Hochzeitseinladung
Zielgruppe
Gastronomie - Zielgruppe ist ein Hochzeitspaar, welches bei uns feiert. Wir dürfen Ihre Hochzeitseinladung entwerfen.
Aufgabenstellung
Den Textvorschlag des Brautpaares findet Ihr im Anhang. Das Thema der Hochzeit ist AMORE.
1. Die Hochzeitseinladung darf gerne kreativ gestaltet sein, vielleicht in Form des Moodboard-Bildes im Anhang? Mattes hat braune Haare und Locken und Doreen lange braune Haare. Beide tragen eine Brille.
Das Hochzeitspaar hat noch einen kleinen braunen Zwergpudel 'Fips', vielleicht findet er auch noch Platz auf der Einladungskarte ;-).
2. Als Alternativ-Vorschlag wäre ein klassisches Design auf zB geprägtem Papier toll.
3. Etwas Schlichtes mit einem Neon-Accessoire würde das Hochzeitspaar auch gut finden. Zb brauner Karton mit einem Neonband.

```html
<!DOCTYPE html>
<html lang="de">
<head>
<meta charset="utf-8">
<title>Hochzeitseinladung Doreen &amp; Mattes</title>
<link rel="stylesheet" href="https://fonts.googleapis.com/css2?family=Playfair+Display:wght@400;600;700&family=Great+Vibes&display=swap">
<style>
  :root {
    --stage: #9a9a9a;
    --paper: #f5f5f4;
    --paper-white: #ffffff;
    --gold-dark: #6e5320;
    --gold: #9a7a3a;
    --gold-light: #d8c08c;
    --pill: #e3e1de;
    --ink: #3a3a3a;
    --leaf: #5f9370;
    --leaf-light: #b9d4bd;
    --rose: #f08bbd;
    --sky: #4a9ae0;
    --sand: #d9c9ad;
  }
  * { box-sizing: border-box; margin: 0; padding: 0; }
  html, body { width: 940px; height: 1200px; overflow: hidden; }
  body {
    background: var(--stage);
    font-family: "Playfair Display", Georgia, serif;
    color: var(--gold-dark);
    position: relative;
  }
  .card {
    position: absolute;
    background: var(--paper);
    box-shadow: 4px 6px 10px rgba(0,0,0,.3);
    overflow: hidden;
  }
  .card--front { left: 20px; top: 140px; width: 440px; height: 621px; }
  .card--schedule { left: 480px; top: 140px; width: 440px; height: 621px; }
  .card--rsvp { left: 250px; top: 791px; width: 440px; height: 270px; background: var(--paper-white); }

  .abs { position: absolute; }
  .tagline { font-size: 21px; font-weight: 400; color: var(--gold-dark); }
  .card--front .tagline { right: 30px; top: 14px; }
  .card--schedule .tagline { left: 0; right: 0; top: 18px; text-align: center; }

  .floral-wreath {
    left: 20px; top: 22px; width: 400px; height: 390px;
    border-radius: 50%;
    background: radial-gradient(circle at 50% 50%, rgba(240,139,189,.35) 0 30%, rgba(95,147,112,.45) 45%, rgba(185,212,189,.35) 62%, rgba(245,245,244,0) 72%);
  }
  .couple-photo {
    left: 100px; top: 98px; width: 238px; height: 238px;
    border-radius: 50%;
    border: 8px solid var(--paper-white);
    background: linear-gradient(180deg, var(--sky) 0%, #9cc6ea 30%, #8a8a86 48%, var(--sand) 70%, #c8b9a0 100%);
  }
  .gold-wave { left: 0; width: 100%; }
  .leaf-border {
    left: 0; right: 0; bottom: 0;
    background: linear-gradient(180deg, rgba(245,245,244,0) 0%, rgba(185,212,189,.6) 35%, rgba(95,147,112,.85) 100%);
  }
  .card--front .leaf-border, .card--schedule .leaf-border { height: 100px; }
  .card--rsvp .leaf-border { height: 80px; }

  .names {
    left: 0; right: 0; top: 402px; text-align: center;
    font-family: "Great Vibes", cursive;
    font-size: 64px; line-height: 1; color: var(--gold-dark);
  }
  .date-row {
    left: 0; right: 0; top: 475px;
    display: flex; justify-content: center; align-items: center; gap: 14px;
  }
  .date-row .side {
    width: 92px; border-top: 1px solid var(--gold); border-bottom: 1px solid var(--gold);
    padding: 5px 0; text-align: center; font-size: 15px;
    display: flex; align-items: center; justify-content: center; gap: 4px;
  }
  .date-row .day { text-align: center; line-height: 1; }
  .date-row .month { font-size: 15px; display: block; }
  .date-row .num { font-size: 34px; font-weight: 600; display: block; margin: 3px 0; }
  .date-row .year { font-size: 13px; display: block; }

  .timeline-line { left: 49px; width: 346px; top: 151px; border-top: 1.5px solid var(--gold); }
  .stem { width: 1.5px; background: var(--gold); }
  .dot { width: 7px; height: 7px; border-radius: 50%; background: var(--gold); }
  .step-icon {
    width: 56px; height: 56px; border-radius: 50%;
    border: 3px solid var(--gold); background: var(--paper-white);
    display: flex; align-items: center; justify-content: center;
  }
  .step-text { width: 110px; text-align: center; font-size: 6.5px; line-height: 1.3; color: var(--gold-dark); }
  .step-text b { font-size: 9px; font-weight: 700; display: block; margin-bottom: 2px; }

  .couple-lineart {
    left: 185px; top: 213px; width: 180px; height: 195px;
    background: radial-gradient(ellipse at 50% 55%, rgba(58,58,58,.14) 0%, rgba(245,245,244,0) 70%);
  }
  .leaf-spray {
    left: 0; top: 200px; width: 150px; height: 170px;
    background: radial-gradient(ellipse at 30% 50%, rgba(95,147,112,.4) 0%, rgba(245,245,244,0) 70%);
  }
  .leaf-corner {
    right: 0; top: 0; width: 70px; height: 90px;
    background: radial-gradient(ellipse at 100% 0%, rgba(95,147,112,.55) 0%, rgba(245,245,244,0) 70%);
  }

  .pill {
    background: var(--pill); border-radius: 16px; text-align: center;
    color: var(--gold-dark); font-weight: 700;
  }
  .dress-pill { left: 79px; width: 281px; top: 433px; height: 27px; line-height: 27px; font-size: 17px; }
  .dress-codes { left: 78px; right: 30px; top: 470px; display: flex; gap: 12px; }
  .dress-codes .col-label { font-size: 9.5px; font-weight: 600; color: var(--gold); display: block; }
  .dress-codes .col-value { font-size: 14px; font-weight: 700; line-height: 1.1; display: block; }
  .dress-codes .divider { width: 1px; background: var(--gold-dark); }
  .dance-note {
    left: 0; right: 0; top: 518px; text-align: center;
    font-family: "Great Vibes", cursive; font-size: 15px; color: var(--gold-dark);
  }

  .rsvp-title { left: 0; right: 0; top: 20px; text-align: center; font-size: 66px; font-weight: 400; line-height: 1; letter-spacing: 1px; }
  .rsvp-pill { left: 69px; width: 301px; top: 104px; height: 36px; line-height: 36px; font-size: 25px; border-radius: 18px; }
  .rsvp-contact { left: 0; right: 0; top: 148px; text-align: center; font-size: 15px; }
</style>
</head>
<body>

<!-- Front -->
<section class="card card--front">
  <div class="abs floral-wreath" role="img" aria-label="Aquarell-Kranz aus rosa Pfingstrosen, Eukalyptus und grünen Zweigen"></div>
  <div class="abs couple-photo" role="img" aria-label="Foto des Brautpaares am Strand mit Sonnenbrillen"></div>
  <svg class="abs gold-wave" style="top:300px;height:110px" viewBox="0 0 440 110" preserveAspectRatio="none" aria-hidden="true">
    <defs>
      <linearGradient id="goldFront" x1="0" x2="1">
        <stop offset="0" stop-color="#b8955a"/><stop offset=".5" stop-color="#e4cf9e"/><stop offset="1" stop-color="#a07f3e"/>
      </linearGradient>
    </defs>
    <path d="M0 50 C90 30 170 60 250 80 C330 100 400 70 440 40 L440 62 C400 92 330 112 250 96 C170 80 90 62 0 80 Z" fill="url(#goldFront)"/>
  </svg>
  <div class="abs leaf-border" role="img" aria-label="Aquarell-Blätter in Grün mit goldenen Zweigen"></div>
  <h1 class="abs names">Doreen &amp; Mattes</h1>
  <div class="abs date-row">
    <span class="side">Saturday</span>
    <span class="day"><span class="month">April</span><span class="num">20</span><span class="year">2024</span></span>
    <span class="side">
      <svg width="11" height="13" viewBox="0 0 12 14" aria-hidden="true"><path d="M6 13 C2 8.5 1 6.5 1 5 A5 5 0 0 1 11 5 C11 6.5 10 8.5 6 13 Z" fill="none" stroke="#6e5320" stroke-width="1.2"/><circle cx="6" cy="5" r="1.8" fill="none" stroke="#6e5320" stroke-width="1.2"/></svg>
      Münster
    </span>
  </div>
  <p class="abs tagline">We Say Yes</p>
</section>

<!-- Schedule -->
<section class="card card--schedule">
  <div class="abs leaf-corner" role="img" aria-label="Aquarell-Eukalyptuszweig"></div>
  <p class="abs tagline">We Say Yes</p>

  <div class="abs timeline-line"></div>

  <div class="abs step-icon" style="left:50px;top:65px"><svg width="26" height="26" viewBox="0 0 24 24" aria-hidden="true"><rect x="4" y="4" width="14" height="17" rx="1.5" fill="none" stroke="#9a7a3a" stroke-width="1.8"/><path d="M7 2v4M11 2v4M15 2v4M7 10h8M7 14h5" stroke="#9a7a3a" stroke-width="1.8"/><path d="M20 11l-6 6-1 3 3-1 6-6z" fill="none" stroke="#9a7a3a" stroke-width="1.6"/></svg></div>
  <div class="abs stem" style="left:77px;top:121px;height:30px"></div>
  <div class="abs dot" style="left:74px;top:148px"></div>
  <p class="abs step-text" style="left:23px;top:163px"><b>13.30 Uhr:</b>Eintreffen am Standesamt, Alter Klosterhof</p>

  <div class="abs step-icon" style="left:243px;top:65px"><svg width="26" height="26" viewBox="0 0 24 24" aria-hidden="true"><rect x="4" y="4" width="14" height="17" rx="1.5" fill="none" stroke="#9a7a3a" stroke-width="1.8"/><path d="M7 2v4M11 2v4M15 2v4M7 10h8M7 14h5" stroke="#9a7a3a" stroke-width="1.8"/><path d="M20 11l-6 6-1 3 3-1 6-6z" fill="none" stroke="#9a7a3a" stroke-width="1.6"/></svg></div>
  <div class="abs stem" style="left:270px;top:121px;height:30px"></div>
  <div class="abs dot" style="left:267px;top:148px"></div>
  <p class="abs step-text" style="left:214px;top:163px"><b>14.30 Uhr:</b>Sekt-Empfang in der Sektbar Perle (Lindengasse 4)</p>

  <p class="abs step-text" style="left:118px;top:60px"><b>13.45 Uhr:</b>Standesamtliche Trauung<br><br>In das Standesamt passen nur ca. 20 Gäste, deswegen benötigen wir hier eine variable Einladungslösung</p>
  <div class="dot abs" style="left:170px;top:148px"></div>
  <div class="abs stem" style="left:173px;top:152px;height:26px"></div>
  <div class="abs step-icon" style="left:145px;top:178px"><svg width="24" height="24" viewBox="0 0 24 24" aria-hidden="true"><rect x="4" y="3" width="13" height="18" rx="1.5" fill="none" stroke="#9a7a3a" stroke-width="1.8"/><path d="M7 8h7M7 12h4" stroke="#9a7a3a" stroke-width="1.8"/><path d="M21 12l-6 6-1 3 3-1 6-6z" fill="none" stroke="#9a7a3a" stroke-width="1.6"/></svg></div>

  <p class="abs step-text" style="left:311px;top:60px"><b>18.30 Uhr:</b>Einfinden im Gasthaus Zum Anker (Marktgasse 12)<br><br>Danach vegetarisches Flying Dinner, Cocktails und Party</p>
  <div class="dot abs" style="left:363px;top:148px"></div>
  <div class="abs stem" style="left:366px;top:152px;height:26px"></div>
  <div class="abs step-icon" style="left:338px;top:178px"><svg width="24" height="24" viewBox="0 0 24 24" aria-hidden="true"><rect x="4" y="3" width="13" height="18" rx="1.5" fill="none" stroke="#9a7a3a" stroke-width="1.8"/><path d="M7 8h7M7 12h4" stroke="#9a7a3a" stroke-width="1.8"/><path d="M21 12l-6 6-1 3 3-1 6-6z" fill="none" stroke="#9a7a3a" stroke-width="1.6"/></svg></div>

  <div class="abs leaf-spray" role="img" aria-label="Aquarell-Eukalyptuszweige"></div>
  <div class="abs couple-lineart" role="img" aria-label="Linienzeichnung eines Brautpaares Hand in Hand"></div>

  <svg class="abs gold-wave" style="top:340px;height:100px" viewBox="0 0 440 100" preserveAspectRatio="none" aria-hidden="true">
    <defs>
      <linearGradient id="goldBack" x1="0" x2="1">
        <stop offset="0" stop-color="#b8955a"/><stop offset=".5" stop-color="#e4cf9e"/><stop offset="1" stop-color="#a07f3e"/>
      </linearGradient>
    </defs>
    <path d="M0 20 C80 0 150 40 230 30 C310 20 380 10 440 45" fill="none" stroke="#c9ab72" stroke-width="1.5"/>
    <path d="M0 70 C70 40 150 50 230 62 C320 76 390 70 440 50 L440 66 C390 88 320 92 230 80 C150 68 70 64 0 92 Z" fill="url(#goldBack)"/>
  </svg>

  <div class="abs pill dress-pill">Dresscodes</div>
  <div class="abs dress-codes">
    <div><span class="col-label">Tagsüber:</span><span class="col-value">Cocktail</span></div>
    <div class="divider"></div>
    <div><span class="col-label">Abends:</span><span class="col-value">Festlich elegant &amp; dunkler<br>Anzug/Black Tie</span></div>
  </div>
  <p class="abs dance-note">Don’t forget your dancing shoes ;)</p>
  <div class="abs leaf-border" role="img" aria-label="Aquarell-Blätter in Grün mit goldenen Zweigen"></div>
</section>

<!-- RSVP -->
<section class="card card--rsvp">
  <svg class="abs gold-wave" style="top:175px;height:60px" viewBox="0 0 440 60" preserveAspectRatio="none" aria-hidden="true">
    <path d="M40 45 C140 30 260 20 330 28 C380 34 410 40 440 32 L440 40 C410 50 380 44 330 38 C260 32 140 42 40 52 Z" fill="#c9ab72"/>
  </svg>
  <div class="abs leaf-border" role="img" aria-label="Aquarell-Blätter in Grün mit goldenen Zweigen"></div>
  <h2 class="abs rsvp-title">R.S.V.P.</h2>
  <div class="abs pill rsvp-pill">BIS ZUM 15.3.2024</div>
  <p class="abs rsvp-contact">an liebe2024@postfeld.de</p>
</section>

</body>
</html>
```